Brain Science Music company needs modern clean website

We're looking for a website that's very clean and modern but also has some nice bold (futuristic) colors in it. The design should communicate a company that's providing something new and fresh! We'd greatly appreciate web designs similar to: https://thebrightfolio.co/

Lumen Cascade is a US-based Neuroscience music company that offers state-of-the-art technology solutions that help people focus, relax and sleep with the help of scientifically engineered music.

Target Market(s)

US businesses looking for specialized neuroscience music technology.

Logo Text

LumenCascade or LC

Coding

Coded - Design and coding required

Number of Pages Required

1 page

Font styles to use
Sans Serif

Colors

Designer to choose colors to be used in the design.

Requirements
Nice to have
• A website similar to: https://thebrightfolio.co/
We like the colors, the fonts, the simple design layouts and the colorful images.

```html
<!DOCTYPE html>
<html lang="en">
<head>
<meta charset="utf-8">
<title>Lumen Cascade — Music and the Brain</title>
<link href="https://fonts.googleapis.com/css2?family=Saira+Condensed:wght@700&family=Montserrat:wght@400;500&display=swap" rel="stylesheet">
<style>
:root{
  --navy:#2e3170;
  --navy-deep:#24285a;
  --blue:#6b87d6;
  --blue-soft:#7f97de;
  --orange:#e98a33;
  --ink:#3a3a55;
  --white:#ffffff;
}
*{margin:0;padding:0;box-sizing:border-box}
html,body{width:1200px;height:2242px;overflow:hidden;background:var(--white)}
body{position:relative;font-family:'Montserrat',sans-serif;color:var(--ink)}
.display{font-family:'Saira Condensed',sans-serif;font-weight:700;color:var(--navy);text-transform:uppercase;letter-spacing:.5px}

.hero-blob{position:absolute;left:0;top:0}
.brand{position:absolute;left:69px;top:18px;font-family:'Saira Condensed',sans-serif;font-weight:700;font-size:18px;line-height:19px;color:var(--navy);text-transform:uppercase}
.main-nav a{position:absolute;top:28px;color:var(--white);font-size:13px;text-decoration:none;letter-spacing:.3px}

.hero-art{position:absolute;left:700px;top:125px;width:420px;height:245px;filter:drop-shadow(0 10px 14px rgba(10,12,40,.35))}
.hero-title{position:absolute;left:69px;top:244px;font-size:58px;line-height:62px}
.learn-more{position:absolute;left:69px;top:376px;color:var(--orange);font-size:20px;font-weight:500;text-decoration:none;letter-spacing:.5px;display:flex;align-items:center;gap:18px}

.section-title{position:absolute;left:0;width:1200px;text-align:center;top:604px;font-size:47px}
.feature-art{position:absolute;width:292px;height:184px;filter:drop-shadow(0 10px 10px rgba(40,50,110,.22))}
.feature-art svg{display:block}
.feature-text{position:absolute;width:400px;text-align:center;font-size:14px;line-height:24.6px;letter-spacing:.7px;word-spacing:2px;white-space:nowrap}

.story-title{position:absolute;left:91px;top:1566px;font-size:56px}
.story-art{position:absolute;left:189px;top:1706px;width:112px;height:140px}
.story-body{position:absolute;left:433px;top:1568px;font-size:15.2px;line-height:28.2px;letter-spacing:.15px;white-space:nowrap}
.story-body p+p{margin-top:28.2px}

.site-footer{position:absolute;left:0;top:2077px;width:1200px;height:165px;background:var(--blue)}
.footer-brand{position:absolute;left:89px;top:29px;font-family:'Saira Condensed',sans-serif;font-weight:700;font-size:18px;line-height:19px;color:var(--navy);text-transform:uppercase}
.footer-nav a{position:absolute;top:30px;color:var(--white);font-size:13px;text-decoration:none;letter-spacing:.3px}
.contact{position:absolute;right:88px;top:30px;text-align:right;color:var(--white)}
.contact .label{font-size:13px}
.contact .line{font-size:11px;margin-top:6px;line-height:17px}
.footer-rule{position:absolute;left:89px;right:88px;top:104px;height:1px;background:var(--navy)}
.copyright{position:absolute;left:89px;top:118px;font-size:9.5px;color:var(--white)}
.social{position:absolute;top:114px;width:20px;height:20px;border-radius:50%;background:var(--navy)}
</style>
</head>
<body>

<svg class="hero-blob" width="1200" height="545" viewBox="0 0 1200 545" aria-hidden="true">
  <defs>
    <linearGradient id="blobFill" x1="0" y1="0" x2="1" y2="1">
      <stop offset="0" stop-color="#3d4282"/>
      <stop offset="1" stop-color="#24285a"/>
    </linearGradient>
  </defs>
  <path d="M470,0 C468,50 500,110 540,160 C578,208 590,260 586,308 C590,345 620,375 703,387 C770,398 810,420 828,470 C850,520 880,538 915,536 C980,532 1060,520 1120,510 C1160,502 1185,492 1200,486 L1200,0 Z" fill="url(#blobFill)"/>
</svg>

<div class="brand">Lumen<br>Cascade</div>

<nav class="main-nav">
  <a style="left:723px">Productivity</a>
  <a style="left:856px">Sleep</a>
  <a style="left:946px">Meditation</a>
  <a style="left:1071px">Athletics</a>
</nav>

<div class="hero-art" role="img" aria-label="Illustration of a listener lying upside down wearing headphones, surrounded by stars and neurons">
  <svg width="420" height="245" viewBox="0 0 420 245" aria-hidden="true">
    <defs>
      <linearGradient id="heroPanel" x1="0" y1="0" x2="1" y2="1">
        <stop offset="0" stop-color="#7a93dd"/>
        <stop offset="1" stop-color="#5d78cc"/>
      </linearGradient>
      <radialGradient id="heroGlow" cx=".5" cy=".5" r=".5">
        <stop offset="0" stop-color="#f3a64f"/>
        <stop offset=".6" stop-color="#e98a33" stop-opacity=".85"/>
        <stop offset="1" stop-color="#e98a33" stop-opacity="0"/>
      </radialGradient>
    </defs>
    <path d="M75,40 L372,18 L320,200 L95,218 Z" fill="url(#heroPanel)"/>
    <ellipse cx="230" cy="125" rx="150" ry="95" fill="url(#heroGlow)" opacity=".55"/>
  </svg>
</div>

<h1 class="hero-title display">The new frontier of<br>music and the brain</h1>
<a class="learn-more">LEARN MORE
  <svg width="24" height="14" viewBox="0 0 24 14" aria-hidden="true"><path d="M1 7H22M16 1L22 7L16 13" fill="none" stroke="#e98a33" stroke-width="1.8"/></svg>
</a>

<h2 class="section-title display">Brainwave entrainment</h2>

<div class="feature-art" style="left:205px;top:730px" role="img" aria-label="Illustration of a neuron on a blue panel">
  <svg width="292" height="184" viewBox="0 0 292 184" aria-hidden="true">
    <defs>
      <linearGradient id="panelA" x1="0" y1="0" x2="1" y2="1"><stop offset="0" stop-color="#7f97de"/><stop offset="1" stop-color="#5f7acd"/></linearGradient>
      <radialGradient id="glowNavy" cx=".5" cy=".5" r=".5"><stop offset="0" stop-color="#2e3170" stop-opacity=".8"/><stop offset="1" stop-color="#2e3170" stop-opacity="0"/></radialGradient>
    </defs>
    <path d="M0,22 L292,0 L247,173 L22,184 Z" fill="url(#panelA)"/>
    <ellipse cx="143" cy="97" rx="100" ry="75" fill="url(#glowNavy)" opacity=".55"/>
  </svg>
</div>
<p class="feature-text" style="left:147px;top:953px">Neurons in our brains communicate with<br>each other, forming thoughts, emotions,<br>and ideas using electrical impulses<br>(commonly known as Brainwaves.)</p>

<div class="feature-art" style="left:704px;top:720px" role="img" aria-label="Illustration of a brain with headphones on a blue panel">
  <svg width="292" height="184" viewBox="0 0 292 184" aria-hidden="true">
    <defs>
      <radialGradient id="glowOrange" cx=".5" cy=".5" r=".5"><stop offset="0" stop-color="#e98a33" stop-opacity=".9"/><stop offset="1" stop-color="#e98a33" stop-opacity="0"/></radialGradient>
    </defs>
    <path d="M0,18 L292,0 L245,172 L22,178 Z" fill="url(#panelA)"/>
    <ellipse cx="120" cy="100" rx="95" ry="70" fill="url(#glowOrange)" opacity=".5"/>
  </svg>
</div>
<p class="feature-text" style="left:651px;top:953px">Activities such as sleeping, working, or<br>meditating, each have their own unique<br>brainwave pattern.</p>

<div class="feature-art" style="left:202px;top:1148px" role="img" aria-label="Illustration of an open head with connected nodes among stars">
  <svg width="292" height="184" viewBox="0 0 292 184" aria-hidden="true">
    <path d="M0,22 L292,0 L246,173 L22,184 Z" fill="url(#panelA)"/>
    <ellipse cx="145" cy="90" rx="100" ry="78" fill="url(#glowNavy)" opacity=".6"/>
    <ellipse cx="145" cy="70" rx="70" ry="40" fill="url(#glowOrange)" opacity=".4"/>
  </svg>
</div>
<p class="feature-text" style="left:147px;top:1373px">Lumen Cascade leverages Musical Phase<br>Locking, to optimize brainwave patterns for<br>each desired activity.</p>

<div class="feature-art" style="left:703px;top:1148px" role="img" aria-label="Illustration of a microscope with music notes">
  <svg width="292" height="184" viewBox="0 0 292 184" aria-hidden="true">
    <path d="M0,22 L292,0 L246,173 L22,184 Z" fill="url(#panelA)"/>
    <ellipse cx="145" cy="95" rx="95" ry="75" fill="url(#glowOrange)" opacity=".45"/>
  </svg>
</div>
<p class="feature-text" style="left:646px;top:1373px">Our music is driven by science. We utilize<br>large scale studies and data from<br>electro-encephlograms to produce<br>substantial results.</p>

<h2 class="story-title display">Julian’s story</h2>
<div class="story-art" role="img" aria-label="Illustration of a notepad and pen">
  <svg width="112" height="140" viewBox="0 0 112 140" aria-hidden="true">
    <defs>
      <linearGradient id="padTone" x1="0" y1="0" x2="1" y2="1"><stop offset="0" stop-color="#e6e9f7"/><stop offset="1" stop-color="#c9d0ee"/></linearGradient>
    </defs>
    <rect x="6" y="30" width="96" height="104" rx="10" fill="url(#padTone)"/>
    <circle cx="98" cy="12" r="10" fill="#e98a33" opacity=".7"/>
  </svg>
</div>
<div class="story-body">
  <p>Founder and Team Leader of Lumen Cascade, in conjunction with primary scientific<br>advisor Dr. Henry Walsh. Julian is a pioneer in the neuroscience of music, and key<br>innovator on the technology of Musical Phase Locking.<br>At the age of 10, Julian wrote his first symphony and began studying<br>music composition. After exposure to alpha waves in music, Julian began a lifelong<br>pursuit of merging neuroscience and music composition.</p>
  <p>Julian founded Clearpath Audio in 2003, creating audio workstations for those who<br>wanted to experience the effects of music guided by neuroscience, as well as software<br>for brain-computer interfaces. As the science progressed and Clearpath Audio grew,<br>Julian decided to form Mindtone in 2014, a website and app that allowed nearly anybody<br>to access the music, not just those who were scientifically minded.</p>
  <p>Lumen Cascade was formed to further the vision of neuroscience-based music<br>becoming a daily resource that everyone should experience.</p>
</div>

<footer class="site-footer">
  <div class="footer-brand">Lumen<br>Cascade</div>
  <nav class="footer-nav">
    <a style="left:397px">Productivity</a>
    <a style="left:530px">Sleep</a>
    <a style="left:620px">Meditation</a>
    <a style="left:745px">Athletics</a>
  </nav>
  <div class="contact">
    <div class="label">Contact</div>
    <div class="line">hello@lumencascade.co<br>adress/phone</div>
  </div>
  <div class="footer-rule"></div>
  <div class="copyright">© 2021 Lumen Cascade - All rights reserved</div>
  <span class="social" style="left:1025px" aria-label="Social profile"></span>
  <span class="social" style="left:1059px" aria-label="Social profile"></span>
  <span class="social" style="left:1092px" aria-label="Social profile"></span>
</footer>

</body>
</html>
```